Baby and kids clothes e-commerce website

We need a clothes ecommerce page with cart and live chat available in English and Spanish. Easy to maintain. Name of the shop is TULAVEN. I need it to be really soft colour palette and easy to navigate. It needs a mobile version.

LOGO NAME "TULAVEN" and there will be a very cute teddy next to it. Picture PELUMain will be the main Bear which could have different accessories such as picture attached PELUkids.

Target Market(s)

25-40 women with kids. Clothes will be quality baby and junior clothing.

Industry/Entity Type

Baby

Logo Text

TULAVEN

Coding

Coded - Design and coding required

Number of Pages Required

5+ page

Requirements
Must have
• It must have a cart, a live chat, account section and newsletter sign up.
• Option to add discounts and change different flash details like in brelvo.com. Also blog feature and all the social Access (including Pinterest). It also needs to have the option to add a product catalogue where products can be selected.
• It will be for baby and junior clothing.
• The 5 pages will be :
• MAIN
• BABY
• GIRLS
• BOYS
• OUTLET
• It needs to have the same pages in both English and Spanish.
Nice to have
• CART
• Account section
• Newsletter sign up
• Product catalogue section
• Discounts and vouchers
• Blog Access
• Social sites including pinterest

```html
<!DOCTYPE html>
<html lang="en">
<head>
<meta charset="utf-8">
<title>TULAVEN — Baby &amp; Kids Wear</title>
<link rel="stylesheet" href="https://fonts.googleapis.com/css2?family=Fredoka:wght@600&family=Open+Sans:wght@400;600;700;800&display=swap">
<style>
  :root{
    --blue:#0a8db1;
    --blue-dark:#086f8d;
    --blue-text:#0a87ab;
    --orange:#ffa600;
    --green:#72ad5e;
    --teal:#08b59d;
    --ink:#263540;
    --grey:#8a8f93;
    --white:#ffffff;
  }
  *{margin:0;padding:0;box-sizing:border-box}
  html,body{width:1200px;height:1200px;overflow:hidden;background:var(--white);font-family:"Open Sans",sans-serif}
  .page{position:relative;width:1200px;height:1200px}
  .masthead{position:absolute;left:0;top:0;width:1200px;height:666px;background:var(--blue)}
  .topbar{position:absolute;left:0;top:0;width:1200px;height:36px;border-bottom:1px dashed rgba(255,255,255,.6)}
  .contact{position:absolute;top:10px;display:flex;align-items:center;gap:6px;color:var(--white);font-size:12px}
  .contact.email{left:124px}
  .contact.phone{left:264px}
  .top-icons{position:absolute;right:140px;top:7px;display:flex;gap:4px}
  .top-icons span{width:22px;height:22px;border-radius:50%;background:var(--white)}
  .brand{position:absolute;left:124px;top:64px;font-weight:800;font-size:40px;color:var(--white);letter-spacing:2px;line-height:1}
  .search{position:absolute;left:773px;top:72px;width:191px;height:32px;border-radius:16px;background:var(--blue-dark);color:var(--white);font-size:12px;padding:8px 16px}
  .search svg{position:absolute;right:16px;top:10px}
  .cart{position:absolute;left:982px;top:66px;display:flex;align-items:flex-end;gap:6px;color:var(--white);font-size:12px;font-weight:600}
  .cart .count{position:absolute;left:10px;top:-4px;width:14px;height:14px;border-radius:50%;background:var(--white);color:#e23a3a;font-size:9px;text-align:center;line-height:14px;font-weight:700}
  .nav{position:absolute;left:124px;top:142px;width:936px;height:44px;background:var(--white);border-radius:3px}
  .nav ul{list-style:none;display:flex;align-items:center;height:44px;padding-left:16px}
  .nav li{font-family:"Fredoka",sans-serif;font-weight:600;font-size:14px;color:var(--grey);letter-spacing:.5px;margin-right:34px}
  .nav li.active{background:var(--blue);color:var(--white);border-radius:16px;padding:7px 17px;margin-right:18px}
  .social{position:absolute;right:8px;top:11px;display:flex;gap:8px}
  .social span{width:24px;height:24px;border-radius:6px;background:#c7d3d9}
  .hero{position:absolute;left:124px;top:198px;width:936px;height:437px;border-radius:3px;overflow:hidden;background:linear-gradient(#f3f3f3,#ffffff 35%,#fafafa 60%)}
  .hero .floor{position:absolute;left:0;top:341px;width:100%;height:96px;background:linear-gradient(#e9e9ea,#f1f1f2)}
  .hero-copy{position:absolute;left:70px;top:58px;width:486px;text-align:center}
  .hero-copy h1{font-family:"Fredoka",sans-serif;font-weight:600;font-size:43px;line-height:47px;color:var(--blue-text);white-space:nowrap}
  .offer{margin-top:16px;font-weight:800;font-size:35px;color:#2a2a2a;line-height:1}
  .offer em{font-style:normal;color:var(--orange)}
  .promo{margin-top:6px;font-size:15px;color:#444}
  .btn-hero{display:inline-block;margin-top:38px;width:166px;height:44px;border-radius:22px;background:var(--orange);color:var(--white);font-weight:800;font-size:18px;line-height:44px}
  .hero-photo{position:absolute;left:566px;top:10px;width:290px;height:420px;border-radius:40% 40% 10% 10%;background:linear-gradient(160deg,#e8c7b0,#9b8fb8 45%,#66c2cf 75%,#f4a38c)}
  .categories{position:absolute;left:123px;top:729px;width:937px;display:flex;gap:23px}
  .cat{position:relative;width:297px;height:185px;border-radius:4px;color:var(--white)}
  .cat::after{content:"";position:absolute;inset:8px;border:1px dashed rgba(255,255,255,.8);border-radius:3px}
  .cat.baby{background:var(--orange)}
  .cat.girls{background:var(--green)}
  .cat.boys{background:var(--teal)}
  .cat-photo{position:absolute;left:22px;top:14px;width:130px;height:171px;border-radius:40% 40% 6px 6px;opacity:.55}
  .cat.baby .cat-photo{background:linear-gradient(#fff7e8,#f2eee6)}
  .cat.girls .cat-photo{background:linear-gradient(#2f9b85,#f2f2f2)}
  .cat.boys .cat-photo{background:linear-gradient(#2a3a5c,#3f6fa8)}
  .cat-text{position:absolute;right:30px;top:40px;width:110px;text-align:center}
  .cat-text h2{font-family:"Fredoka",sans-serif;font-weight:600;font-size:28px;line-height:32px}
  .cat-text .btn{display:inline-block;margin-top:8px;width:96px;height:28px;border-radius:14px;background:var(--white);font-weight:700;font-size:13px;line-height:28px}
  .cat.baby .btn{color:var(--orange)}
  .cat.girls .btn{color:var(--green)}
  .cat.boys .btn{color:var(--teal)}
  .deals-title{position:absolute;left:0;top:972px;width:1200px;text-align:center;font-family:"Fredoka",sans-serif;font-weight:600;font-size:35px;color:var(--blue-text)}
  .divider{position:absolute;left:509px;top:1015px}
  .deal{position:absolute;top:1082px;height:140px;border:1px dashed #3aa79a;border-bottom:none;border-radius:4px}
  .deal.lifetime{left:124px;width:451px}
  .deal.showroom{left:607px;width:452px}
  .deal-photo{position:absolute;top:14px;height:130px;border-radius:3px}
  .deal.lifetime .deal-photo{left:28px;width:216px;background:linear-gradient(#f8f8f8,#f2d7c5 50%,#e7a6b7)}
  .deal.showroom .deal-photo{left:18px;width:240px;background:linear-gradient(#f2f2f2,#e6e6ea 60%,#d9c3cf)}
  .deal h3{position:absolute;top:60px;font-family:"Fredoka",sans-serif;font-weight:600;font-size:26px;line-height:28px;color:var(--ink)}
  .deal.lifetime h3{left:299px}
  .deal.showroom h3{left:289px}
</style>
</head>
<body>
<div class="page">
  <header class="masthead">
    <div class="topbar">
      <div class="contact email">
        <svg width="18" height="14" viewBox="0 0 18 14"><rect x="1" y="1" width="16" height="12" fill="none" stroke="#fff" stroke-width="1.3"/><path d="M1 1l8 7 8-7M1 13l6-6M17 13l-6-6" fill="none" stroke="#fff" stroke-width="1.2"/></svg>
        info@tulaven.com
      </div>
      <div class="contact phone">
        <svg width="12" height="16" viewBox="0 0 12 16"><path d="M3 1l2 3-1.5 1.5c.5 2 2 4.5 4 6L9 10l2.5 2.5-2 2C5 14 1.5 8 1.5 3z" fill="#fff"/></svg>
        1800 482 917
      </div>
      <div class="top-icons"><span></span><span></span><span></span></div>
    </div>

    <div class="brand">TULAVEN</div>

    <div class="search">Search
      <svg width="11" height="11" viewBox="0 0 11 11"><circle cx="4.5" cy="4.5" r="3.5" fill="none" stroke="#fff" stroke-width="1.4"/><path d="M7 7l3 3" stroke="#fff" stroke-width="1.4"/></svg>
    </div>

    <div class="cart">
      <svg width="34" height="30" viewBox="0 0 34 30"><path d="M1 4h5l4 16h18l4-12H8" fill="none" stroke="#fff" stroke-width="1.6"/><circle cx="13" cy="26" r="2" fill="none" stroke="#fff" stroke-width="1.4"/><circle cx="25" cy="26" r="2" fill="none" stroke="#fff" stroke-width="1.4"/></svg>
      <span class="count">2</span>
      <span style="margin-bottom:12px">My Cart</span>
    </div>

    <nav class="nav">
      <ul>
        <li class="active">HOME</li>
        <li>MAIN</li>
        <li>BABY</li>
        <li>GIRLS</li>
        <li>BOYS</li>
        <li>OUTLET</li>
      </ul>
      <div class="social"><span></span><span></span><span></span><span></span><span></span></div>
    </nav>

    <section class="hero">
      <div class="floor"></div>
      <div class="hero-copy">
        <h1>funky everyday wear<br>for babies &amp; kids</h1>
        <p class="offer">FLAT <em>50%</em> OFF</p>
        <p class="promo">PROMOCODE : KIDS50 &nbsp;|&nbsp; ON $999</p>
        <span class="btn-hero">SHOP NOW</span>
      </div>
      <div class="hero-photo" role="img" aria-label="Photo of a boy and a girl in colourful striped knitwear and jeans"></div>
    </section>
  </header>

  <section class="categories">
    <article class="cat baby">
      <div class="cat-photo" role="img" aria-label="Photo of a baby in a white romper"></div>
      <div class="cat-text"><h2>Baby<br>Wear</h2><span class="btn">SHOP NOW</span></div>
    </article>
    <article class="cat girls">
      <div class="cat-photo" role="img" aria-label="Photo of a girl in a printed party dress"></div>
      <div class="cat-text"><h2>Girls<br>Wear</h2><span class="btn">SHOP NOW</span></div>
    </article>
    <article class="cat boys">
      <div class="cat-photo" role="img" aria-label="Photo of a boy in a navy jacket and jeans"></div>
      <div class="cat-text"><h2>Boys<br>Wear</h2><span class="btn">SHOP NOW</span></div>
    </article>
  </section>

  <h2 class="deals-title">Deals Of The Week</h2>
  <svg class="divider" width="182" height="34" viewBox="0 0 182 34">
    <path d="M0 16h70M112 16h70" stroke="#b9bec2" stroke-width="1"/>
    <circle cx="91" cy="16" r="12" fill="none" stroke="#b9bec2" stroke-width="1.4"/>
  </svg>

  <article class="deal lifetime">
    <div class="deal-photo" role="img" aria-label="Photo of a group of smiling children in bright t-shirts"></div>
    <h3>Once in a<br>Lifetime</h3>
  </article>
  <article class="deal showroom">
    <div class="deal-photo" role="img" aria-label="Photo of a bright kids clothing showroom interior"></div>
    <h3>Visit Our<br>Showroom</h3>
  </article>
</div>
</body>
</html>
```